Invitation for Annual Banquet

We would like an invitation designed for our annual banquet that depicts a bridge. We need your creative talent to come up with a theme. We are wanting to project that we are building a bridge to the future: a better future, a more prosperous future. We would like our logo colors incorporated or at least compliment the logo. We will be incorporating the graphics into the program as well. The event details are as follows: The Board of Directors and staff cordially invite you to attend the 82nd Annual Meeting & Mini Business Expo ~ Tuesday, February 4, 2020 ~ 5:45 P.M. Social, 6:15 P. M. Dinner ~ Larkmoor Church, 4918 Corwin P Dalby Rd S, Brennfield ~ Please RSVP by January 27, 2020
I don't know exactly!!

```html
<!DOCTYPE html>
<html lang="en">
<head>
<meta charset="utf-8">
<title>82nd Annual Meeting Invitation</title>
<link rel="stylesheet" href="https://fonts.googleapis.com/css2?family=Roboto:wght@300;400;500;700&display=swap">
<style>
  :root {
    --page: #f1f2f4;
    --card: #ffffff;
    --navy: #1f3590;
    --ink: #2e3f9c;
    --orange: #ee8a2c;
    --steel-dark: #0b2a55;
    --steel: #2f6fb0;
    --steel-light: #cfe2f3;
  }
  * { margin: 0; padding: 0; box-sizing: border-box; }
  html, body { width: 863px; height: 1200px; overflow: hidden; }
  body {
    background: var(--page);
    font-family: "Roboto", Arial, sans-serif;
    position: relative;
  }
  .card {
    position: absolute;
    left: 148px;
    width: 598px;
    background: var(--card);
    overflow: hidden;
    box-shadow: 0 2px 6px rgba(0,0,0,0.12);
  }
  .card--front { top: 88px; height: 420px; }
  .card--back { top: 678px; height: 424px; }

  .walkway-photo {
    position: absolute;
    inset: 0;
    background:
      radial-gradient(ellipse 55% 60% at 10% 100%, rgba(255,255,255,0.95) 0%, rgba(255,255,255,0.6) 45%, rgba(255,255,255,0) 75%),
      radial-gradient(ellipse 30% 40% at 42% 38%, rgba(255,255,255,0.35), rgba(255,255,255,0) 70%),
      linear-gradient(160deg, var(--steel-dark) 0%, var(--steel) 45%, var(--steel-light) 100%);
  }

  .theme-band {
    position: absolute;
    top: 66px;
    left: 408px;
    right: 0;
    height: 76px;
    background: var(--orange);
    opacity: 0.92;
    color: #fff;
    padding: 9px 0 0 30px;
  }
  .theme-band__lead {
    display: block;
    font-weight: 300;
    font-size: 18px;
    line-height: 1.1;
    letter-spacing: 0.3px;
    opacity: 0.85;
  }
  .theme-band__title {
    display: block;
    font-weight: 400;
    font-size: 36px;
    line-height: 1.1;
    letter-spacing: 0.3px;
  }

  .org-name {
    position: absolute;
    color: var(--navy);
    line-height: 1;
  }
  .org-name__main { display: block; font-weight: 700; }
  .org-name__sub { display: block; font-weight: 400; }
  .card--front .org-name { left: 21px; top: 354px; }
  .card--front .org-name__main { font-size: 29px; letter-spacing: -0.2px; }
  .card--front .org-name__sub { font-size: 13px; margin-top: 3px; letter-spacing: 5.4px; }
  .card--back .org-name { left: 364px; top: 104px; }
  .card--back .org-name__main { font-size: 20px; letter-spacing: -0.1px; }
  .card--back .org-name__sub { font-size: 10px; margin-top: 3px; letter-spacing: 3.5px; }

  .invitation {
    position: absolute;
    left: 90px;
    top: 180px;
    color: var(--ink);
    font-size: 17px;
    font-weight: 400;
    line-height: 21px;
  }
  .invitation__lead { margin-bottom: 40px; }
  .invitation__details { margin-bottom: 21px; }
  .invitation__event { font-weight: 500; }
</style>
</head>
<body>
  <section class="card card--front">
    <div class="walkway-photo" role="img" aria-label="Photo of a long glass-walled moving walkway receding into a bright blue distance"></div>
    <div class="theme-band">
      <span class="theme-band__lead">BRIDGE TO THE</span>
      <span class="theme-band__title">FUTURE</span>
    </div>
    <div class="org-name">
      <span class="org-name__main">HARLOW CHAMBER</span>
      <span class="org-name__sub">OF COMMERCE &amp; TOURISM</span>
    </div>
  </section>

  <section class="card card--back">
    <div class="org-name">
      <span class="org-name__main">HARLOW CHAMBER</span>
      <span class="org-name__sub">OF COMMERCE &amp; TOURISM</span>
    </div>
    <div class="invitation">
      <p class="invitation__lead">The Board of Directors and staff cordially invite you<br>to attend the <span class="invitation__event">82nd Annual Meeting &amp; Mini Business</span></p>
      <p class="invitation__details">Expo ~ Tuesday, February 4, 2020 ~ 5:45 P.M.<br>Social, 6:15 P. M. Dinner ~ Larkmoor Church, 4918<br>Corwin P Dalby Rd S, Brennfield</p>
      <p class="invitation__rsvp">Please RSVP by January 27, 2020</p>
    </div>
  </section>
</body>
</html>
```